Kelvora Painting Services Requires a New Responsive Site

Hi Designers,

Our current website is this www.kelvorapainting.com.au for some idea.
I made it on Adobe Muse, its very basic.
I would like it to be redesigned to look more professional and also responsive. I actually know how to do html5 and css but I think others will do this much better than me.

I do not need content because I am a copywriter and would like to do all SEO and copy myself.

The most improtant things to remember is that the site cannot use a CMS
and the code needs to be understandable so that I can go in and add content later on and do SEO work.

Also the site requires an additional testimonial page. I would imagine a nice gallery would be a great addition too(something that I can add images too through html. Also in it is important for it to contain those brand images on the front page as it increases authority. I will attach them onto the brief.

Those two files of findnest and citybookly are local directories where we have reviews so a placement of those on the testimonail page would make great sense. I will to the href myself.

Anyway, good luck!

I look forward to see your designs :D

I have just been informed that on this site websites are simply designed and not built (developed) if this is the case please stop working on your designs and spending more time on this project. I REQUIRE DEVELOPMENT ALSO AND HAVE ALREADY CONTACTED SUPPORT.

Target Market(s)

The target market is 30-75 high income earners.

Industry/Entity Type

Painting

Number of Pages Required

5+ page

Font styles to use
Serif
Sans Serif

Requirements
Must have
• attractive gallery, and the brand icons uploaded.
• must be responsive
• web carousel (with the different types of work we do). eg domestic, commercial, industrial etc.
Nice to have
• a little interactivity
• corporate a natural design that goes well with our logo
Should not have
• any content. just write jiberish to fill in the spaces.
• I will be doing all copy and SEO myself.
• More than five pages, bascially the four that already exist plus the testimonail one.

```html
<!DOCTYPE html>
<html lang="en">
<head>
<meta charset="utf-8">
<title>Kelvora Painting</title>
<link href="https://fonts.googleapis.com/css2?family=Mulish:wght@300;400;600;700&family=Open+Sans:wght@400;600&display=swap" rel="stylesheet">
<style>
:root{
  --header-top:#3c3c3c;
  --header-bottom:#4b4b4b;
  --accent:#4aa3df;
  --sky:#5ab4e6;
  --caption:rgba(76,152,208,.88);
  --button:#2e5877;
  --ink:#3a3a3a;
  --muted:#8a8a8a;
  --rule:#e2e2e2;
  --footer:#323740;
  --footer-text:#8b919b;
  --white:#fff;
}
*{margin:0;padding:0;box-sizing:border-box}
html,body{width:713px;height:1200px;overflow:hidden;background:var(--white)}
body{position:relative;font-family:"Open Sans",sans-serif;color:var(--ink)}
.abs{position:absolute}

/* header */
.site-header{left:0;top:0;width:713px;height:82px;background:linear-gradient(var(--header-top),var(--header-bottom));border-bottom:1px solid #2c2c2c}
.brand{left:87px;top:11px;display:flex;align-items:center;gap:10px}
.brand-mark{width:58px;height:58px;background:var(--accent)}
.brand-name{font-family:"Mulish",sans-serif;font-weight:400;font-size:16px;line-height:20px;color:var(--white)}
.enquiry{right:105px;top:16px;text-align:right;font-family:"Mulish",sans-serif}
.enquiry-label{font-size:10px;color:#ddd}
.enquiry-phone{display:flex;align-items:center;gap:5px;font-size:13px;color:var(--accent)}
.main-nav{left:309px;top:56px;display:flex;gap:22px;font-family:"Mulish",sans-serif;font-size:9.5px;font-weight:600;color:var(--white)}
.main-nav .active{position:relative}
.main-nav .active::after{content:"";position:absolute;left:-7px;right:-7px;top:24px;height:3px;background:var(--accent)}

/* hero */
.hero{left:0;top:83px;width:713px;height:292px}
.hero-photo{width:100%;height:100%;
  background:
    linear-gradient(180deg,rgba(0,0,0,0) 0%,rgba(0,0,0,0) 72%,rgba(60,30,10,.55) 100%),
    linear-gradient(90deg,#7a4e26 0%,#b07a45 12%,#d8dadc 15%,#f0f0ee 22%,#c8621f 27%,#d9742c 55%,#c9682a 75%,#a8561e 100%)}
.hero-caption{left:86px;top:89px;width:240px;height:99px;background:var(--caption);padding:16px 0 0 21px;color:var(--white);font-family:"Mulish",sans-serif}
.hero-caption h1{font-weight:400;font-size:17px;line-height:20px}
.hero-caption h2{font-weight:300;font-size:15px;line-height:20px}
.hero-caption p{font-size:6.5px;line-height:11px;margin-top:4px;color:#e6f1fa}
.hero-arrow{top:110px}

/* services */
.services{left:88px;top:394px;width:540px;display:flex;justify-content:space-between}
.service{width:124px;text-align:center}
.service-icon{width:61px;height:61px;border:2px solid #ddd;border-radius:50%;margin:0 auto;display:flex;align-items:center;justify-content:center}
.service h3{font-family:"Mulish",sans-serif;font-weight:400;font-size:12px;margin-top:5px;color:var(--ink)}
.service p{font-size:5.6px;line-height:10px;color:var(--muted);margin-top:2px}
.read-more{display:inline-block;margin-top:4px;width:61px;height:17px;line-height:17px;background:var(--button);color:var(--white);font-size:7px;border-radius:2px;font-family:"Mulish",sans-serif;font-weight:600}

.divider{left:85px;top:554px;width:536px;height:1px;background:var(--rule)}

/* about */
.about{left:110px;top:574px;width:493px;text-align:center}
.about h2{font-family:"Mulish",sans-serif;font-weight:300;font-size:19px;color:#333}
.about p{font-size:6.6px;line-height:11.3px;color:#555;margin-top:7px}

/* gallery */
.gallery-band{left:0;top:713px}
.gallery-title{left:0;top:736px;width:713px;display:flex;align-items:center;justify-content:center;gap:10px;font-family:"Mulish",sans-serif;font-weight:300;font-size:19px;color:var(--white)}
.gallery-title span.rule{width:103px;height:1px;background:rgba(255,255,255,.4)}
.gallery-grid{left:108px;top:780px;display:grid;grid-template-columns:repeat(4,118px);gap:6px 7px}
.gallery-item{height:74px;border:3px solid var(--white);box-shadow:0 2px 6px rgba(0,0,0,.15)}

/* partners */
.partners{left:112px;top:1025px;width:486px;display:flex;align-items:center;justify-content:space-between;font-family:"Mulish",sans-serif;font-weight:700}
.partner-badge{width:46px;height:46px}
.partner-name{font-size:13px;color:#2a2a2a}

/* footer */
.site-footer{left:0;top:1108px;width:713px;height:92px;background:var(--footer)}
.footer-item{top:22px;display:flex;gap:8px;font-size:6.5px;line-height:9px;color:var(--footer-text);white-space:nowrap}
.footer-item strong{display:block;font-family:"Mulish",sans-serif;font-size:7.5px;line-height:10px;color:#b4bac3}
.footer-social{left:590px;top:24px;width:22px;height:22px;background:#d6402f;border-radius:2px}
.footer-rule{left:107px;top:62px;width:500px;height:1px;background:#3f4550}
.copyright{left:0;top:74px;width:713px;text-align:center;font-size:6.5px;color:#6d737c}
</style>
</head>
<body>

<header class="site-header abs">
  <div class="brand abs">
    <span class="brand-mark"></span>
    <span class="brand-name">Kelvora<br>Painting</span>
  </div>
  <div class="enquiry abs">
    <div class="enquiry-label">For Enquiry</div>
    <div class="enquiry-phone">
      <svg width="17" height="17" viewBox="0 0 20 20"><circle cx="10" cy="10" r="8.5" fill="none" stroke="#fff" stroke-width="1.5"/><path d="M7 5.5c1 0 1.5 2 1.3 2.6-.3.6-.9.6-.5 1.6.4 1 1.3 1.9 2.2 2.3.9.4 1-.2 1.6-.5.6-.3 2.6.4 2.6 1.3 0 .8-1 1.8-2 1.8-3.5 0-6.8-3.3-6.8-6.8 0-1 .9-2.3 1.6-2.3z" fill="#fff"/></svg>
      1300 555 014
    </div>
  </div>
  <nav class="main-nav abs">
    <span class="active">HOME</span><span>ABOUT US</span><span>SERVICES</span><span>GALLERY</span><span>CONTACT US</span>
  </nav>
</header>

<section class="hero abs">
  <div class="hero-photo" role="img" aria-label="Modern living room with orange feature wall, timber panelling and a wall-mounted television"></div>
  <div class="hero-caption abs">
    <h1>Curabitur iaculis tempus</h1>
    <h2>Mauris vel lacus vitae felis</h2>
    <p>Curabitur iaculis tempus eros Curabitur vel mi sit amet<br>magna malesuada ultrices Ut nisi erat fermentu</p>
  </div>
  <svg class="hero-arrow abs" style="left:40px" width="20" height="46" viewBox="0 0 20 46"><path d="M18 2 2 23l16 21" fill="none" stroke="rgba(255,255,255,.5)" stroke-width="1.5"/></svg>
  <svg class="hero-arrow abs" style="left:648px" width="20" height="46" viewBox="0 0 20 46"><path d="M2 2l16 21L2 44" fill="none" stroke="rgba(255,255,255,.5)" stroke-width="1.5"/></svg>
</section>

<section class="services abs">
  <article class="service">
    <div class="service-icon"><svg width="34" height="30" viewBox="0 0 34 30"><path d="M17 2 2 15h4v13h8v-8h6v8h8V15h4z" fill="#3a9ad9"/></svg></div>
    <h3>Domestic Painting</h3>
    <p>Curabitur iaculis tempus eros Curabitur vel mi sit amet magna malesuada ultrices Ut fermentum</p>
    <span class="read-more">READ MORE</span>
  </article>
  <article class="service">
    <div class="service-icon"><svg width="26" height="34" viewBox="0 0 26 34"><path d="M3 2h20v30H3z" fill="#3a9ad9"/><g fill="#fff"><rect x="7" y="6" width="4" height="4"/><rect x="15" y="6" width="4" height="4"/><rect x="7" y="13" width="4" height="4"/><rect x="15" y="13" width="4" height="4"/><rect x="7" y="20" width="4" height="4"/><rect x="15" y="20" width="4" height="4"/></g></svg></div>
    <h3>Commercial Painting</h3>
    <p>Curabitur iaculis tempus eros Curabitur vel mi sit amet magna malesuada ultrices Ut fermentum</p>
    <span class="read-more">READ MORE</span>
  </article>
  <article class="service">
    <div class="service-icon"><svg width="38" height="28" viewBox="0 0 38 28"><path d="M2 26V12l8-4v4l8-4v4l8-4V2h4v6h4v18z" fill="#3a9ad9"/><g fill="#fff"><rect x="6" y="17" width="3" height="3"/><rect x="13" y="17" width="3" height="3"/><rect x="20" y="17" width="3" height="3"/></g></svg></div>
    <h3>Industrial Painting</h3>
    <p>Curabitur iaculis tempus eros Curabitur vel mi sit amet magna malesuada ultrices Ut fermentum</p>
    <span class="read-more">READ MORE</span>
  </article>
  <article class="service">
    <div class="service-icon"><svg width="32" height="36" viewBox="0 0 32 36"><path d="M15 1h2v4h3v2h-3v4l5 5h8v18H2V16h8l5-5V7h-3V5h3z" fill="#3a9ad9"/><path d="M14 34v-6a2 2 0 0 1 4 0v6z" fill="#fff"/><rect x="5" y="21" width="3" height="4" fill="#fff"/><rect x="24" y="21" width="3" height="4" fill="#fff"/></svg></div>
    <h3>Heritage Painting</h3>
    <p>Curabitur iaculis tempus eros Curabitur vel mi sit amet magna malesuada ultrices Ut fermentum</p>
    <span class="read-more">READ MORE</span>
  </article>
</section>

<div class="divider abs"></div>

<section class="about abs">
  <h2>About Our Company</h2>
  <p>Kelvora Painting is an Australian family owned Painting &amp; Decorating business based in Larrow, in the south east of Melbourne. We proudly provide domestic and commercial painting services across all suburbs of metropolitan Melbourne</p>
  <p>Mauris vel lacus vitae felis vestibulum volutpat Etiam est nunc venenatis in tristique eu imperdiet ac nisl Cum sociis natoque penatibus et magnis dis parturient montes nascetur ridiculus mus In iaculis facilisis massa Etiam eu urna Sed porta Suspendisse quam leo molestie sed luctus quis feuMauris vel lacus vitae felis vestibulum volutpat Etiam est nunc venenatis in tristique eu imperdiet ac nisl Cum sociis natoque penatibus et magnis dis parturient montes nascetur ridiculus mus In iaculis facilisis massa Etiam eu urna Sed porta Suspendisse quam leo molestie sed luctus</p>
</section>

<svg class="gallery-band abs" width="713" height="275" viewBox="0 0 713 275">
  <path d="M0 0h713v219L356 272 0 233z" fill="#5ab4e6"/>
  <path d="M0 215c120 12 250 22 356 57L0 237z" fill="#e9f3fa"/>
  <path d="M0 213c120 14 250 24 356 59L0 224z" fill="#fff"/>
</svg>
<h2 class="gallery-title abs"><span class="rule"></span>Our Gallery<span class="rule"></span></h2>
<div class="gallery-grid abs">
  <div class="gallery-item" role="img" aria-label="Green painted room with white chair" style="background:linear-gradient(90deg,#8fb86a,#5e8f45 45%,#e6ebe0 75%,#9fbf8a)"></div>
  <div class="gallery-item" role="img" aria-label="Pale blue room with chandelier and timber floor" style="background:linear-gradient(#a8cde0,#cfe2ec 62%,#9a6a3c 64%,#7a4f2a)"></div>
  <div class="gallery-item" role="img" aria-label="Empty cream room with timber floor" style="background:linear-gradient(#2e3a5a 0%,#4a5a80 20%,#eeeae0 22%,#f2eee6 70%,#c49a5a 72%,#b0854a)"></div>
  <div class="gallery-item" role="img" aria-label="Living room with blue feature wall and sofa" style="background:linear-gradient(#e8eef2 0%,#4a9ec2 20%,#3a8fb8 62%,#e4e4e4 64%,#cfcfcf)"></div>
  <div class="gallery-item" role="img" aria-label="Red walled lounge with timber furniture" style="background:linear-gradient(#d0604a,#c5533a 45%,#a86a3c 50%,#c9965e)"></div>
  <div class="gallery-item" role="img" aria-label="White dining room with table and chairs" style="background:linear-gradient(#eae6df,#f6f4ef 65%,#d9c9a8 70%,#c8a978)"></div>
  <div class="gallery-item" role="img" aria-label="Blue hallway with white staircase" style="background:linear-gradient(90deg,#b8d8e6,#cfe3ec 50%,#f2f4f4 60%,#6a5a4a)"></div>
  <div class="gallery-item" role="img" aria-label="Beige room with archway and timber floor" style="background:linear-gradient(#e6dcc0,#d8c8a0 60%,#9a6230 63%,#7a4a22)"></div>
</div>

<section class="partners abs">
  <span class="partner-badge" style="background:#1e9ad6" aria-label="findnest"></span>
  <span class="partner-badge" style="background:#1a3f86;border-radius:50%" aria-label="warranty badge"></span>
  <span class="partner-name">Larkmere</span>
  <span class="partner-badge" style="width:36px;height:40px;background:#f3d300" aria-label="citybookly"></span>
  <span class="partner-name">Corvell</span>
  <span class="partner-name" style="color:#1a2f78">Brightwell</span>
</section>

<footer class="site-footer abs">
  <div class="footer-item abs" style="left:106px">
    <svg width="14" height="22" viewBox="0 0 14 22"><path d="M7 0a7 7 0 0 1 7 7c0 5-7 15-7 15S0 12 0 7a7 7 0 0 1 7-7z" fill="#5b616b"/><circle cx="7" cy="7" r="2.6" fill="#323740"/></svg>
    <div><strong>Address</strong>Larrow Victoria 3906,<br>Australia</div>
  </div>
  <div class="footer-item abs" style="left:210px">
    <svg width="22" height="16" viewBox="0 0 22 16"><rect width="22" height="16" fill="#5b616b"/><path d="M0 0l11 9 11-9" fill="none" stroke="#323740" stroke-width="1.5"/></svg>
    <div><strong>Email</strong>info@kelvorapainting.com.au</div>
  </div>
  <div class="footer-item abs" style="left:349px">
    <svg width="18" height="18" viewBox="0 0 20 20"><path d="M4 1c2 0 3 4 2.6 5.2-.6 1.2-1.8 1.2-1 3.2.8 2 2.6 3.8 4.4 4.6 1.8.8 2-.4 3.2-1 1.2-.6 5.2.8 5.2 2.6 0 1.6-2 3.6-4 3.6C7.4 19.2 1 12.6 1 5.6 1 3.6 2.6 1 4 1z" fill="#5b616b"/></svg>
    <div><strong>Email</strong>info@kelvorapainting.com.au</div>
  </div>
  <span class="footer-social abs" aria-label="social profile"></span>
  <div class="footer-rule abs"></div>
  <p class="copyright abs">© 2014 Kelvora Painting All rights reserved</p>
</footer>

</body>
</html>
```